SKY Renting ( Website Graphic design ) small property management new business ( real estate )

I need a website designed for a new small Property Management ( no sales ) company I'm starting up soon. I have a design in mind that I like and would like to keep it quite similar to this if possible using my logo and colour scheme and slightly ALTER the layout. and maybe a little more interactive with some motion and images etc
Please see the link to show the simplicity I'm after. I want to be bold ad very clear and concise. I love the simplicity of this design but not necessarily the pages with just text on them. I would want them to be a bit more interesting with some pictures and photos. http://www.tilvanmorebay.com.au/

The branding on the site should be bold and very sharp.

My target market is the mid to high end of the rental market in Darwin Australia and should reflect "good quality, outstanding service and attention to detail, energetic, integrity, "

I will only require a few pages to start with, Home / Company Profile / Management Services / Owners information / Tenant information / Properties and About Darwin. I will be able to provide text for each of the pages but would be no more than 4-6 paragraphs apart from the management services page which would detail a number of the services we would offer. The properties page will just be a link to homefindr,com.au to show my listings and then a couple more links to owner and tenant portals, facebook page etc. It must also be responsive to mobile devices.

I would also like to include a facebook page design and build.

regards
Maren Pickett

Target Market(s)

property owners, investors, Darwin Australia, renters, ages 30 - 60, tenants

Industry/Entity Type

Property Management

Font styles to use
Other font styles liked:
• i like helvetica, but not essential

Requirements
Must have
• Clean and crisp pages, not busy , responsive to devices
• links to portals and facebook, any ability to add other links at a later date.
Nice to have
• music - must be upbeat but not over the top
Should not have
• be too busy on each page

```html
<!DOCTYPE html>
<html lang="en">
<head>
<meta charset="utf-8">
<title>SKY Renting — Property Management Darwin</title>
<link rel="stylesheet" href="https://fonts.googleapis.com/css2?family=Open+Sans:wght@300;400&display=swap">
<style>
  :root {
    --teal: #008a8f;
    --charcoal: #4a4647;
    --paper: #ffffff;
  }
  html, body {
    margin: 0;
    padding: 0;
    width: 1200px;
    height: 876px;
    overflow: hidden;
    background: var(--teal);
  }
  .home-canvas {
    display: block;
    width: 1200px;
    height: 876px;
  }
  .tile-dark { fill: var(--charcoal); }
  .tile-light { fill: var(--paper); }
  .tile-label {
    font-family: "Open Sans", Helvetica, Arial, sans-serif;
    font-size: 21px;
    font-weight: 400;
  }
  .tile-label--on-dark { fill: var(--paper); }
  .tile-label--on-light { fill: var(--teal); }
  .icon-on-dark { fill: var(--paper); }
  .icon-on-light { fill: var(--teal); }
  .icon-line-light { fill: none; stroke: var(--teal); stroke-width: 4; }
  .brand-name {
    font-family: "Open Sans", Helvetica, Arial, sans-serif;
    font-weight: 300;
    fill: var(--paper);
  }
</style>
</head>
<body>
<svg class="home-canvas" viewBox="0 0 1440 1051" xmlns="http://www.w3.org/2000/svg" aria-label="SKY Renting home navigation">
  <defs>
    <clipPath id="brand-tile-clip">
      <rect x="128" y="272" width="260" height="260" transform="rotate(-32.4)"/>
    </clipPath>
  </defs>

  <!-- Brand tile -->
  <g class="brand-tile">
    <rect class="tile-dark" x="128" y="272" width="260" height="260" transform="rotate(-32.4)"/>
    <g clip-path="url(#brand-tile-clip)">
      <text class="brand-name" x="337" y="162" font-size="84">SKY</text>
      <text class="brand-name" x="337" y="232" font-size="46">Renting</text>
    </g>
  </g>

  <g class="tile-grid" transform="rotate(-32.4)">

    <!-- Owners information -->
    <g class="nav-tile nav-tile--owners" transform="translate(8 546)">
      <rect class="tile-light" width="260" height="260"/>
      <g class="tile-icon" transform="translate(44 22)">
        <rect class="icon-on-light" x="0" y="0" width="36" height="44" rx="2"/>
        <rect fill="#fff" x="6" y="8" width="24" height="3"/>
        <rect fill="#fff" x="6" y="15" width="24" height="3"/>
        <rect fill="#fff" x="6" y="22" width="24" height="3"/>
        <rect fill="#fff" x="6" y="29" width="16" height="3"/>
        <rect class="icon-on-light" x="-6" y="38" width="22" height="10" rx="4"/>
      </g>
      <text class="tile-label tile-label--on-light" transform="translate(21 17) rotate(90)">Owners information</text>
    </g>

    <!-- Company Profile -->
    <g class="nav-tile nav-tile--company" transform="translate(236 544)">
      <rect class="tile-dark" width="260" height="260"/>
      <g class="tile-icon" transform="translate(18 170)">
        <path class="icon-on-dark" d="M0 6 h18 l5 6 h27 v34 h-50 z"/>
        <path fill="var(--charcoal)" d="M4 20 h46 l-6 24 h-44 z"/>
        <path class="icon-on-dark" d="M8 22 h44 l-6 22 h-44 z"/>
      </g>
      <text class="tile-label tile-label--on-dark" x="16" y="238">Company Profile</text>
    </g>

    <!-- Management Services -->
    <g class="nav-tile nav-tile--management" transform="translate(465 576)">
      <rect class="tile-light" width="260" height="260"/>
      <g class="tile-icon" transform="translate(42 24)">
        <rect class="icon-line-light" x="0" y="4" width="44" height="40"/>
        <line class="icon-line-light" x1="8" y1="12" x2="36" y2="38"/>
        <line class="icon-line-light" x1="36" y1="12" x2="8" y2="38"/>
        <rect class="icon-on-light" x="-4" y="44" width="52" height="5"/>
      </g>
      <text class="tile-label tile-label--on-light" transform="translate(20 16) rotate(90)">Management Services</text>
    </g>

    <!-- About Darwin -->
    <g class="nav-tile nav-tile--darwin" transform="translate(-24 834)">
      <rect class="tile-dark" width="260" height="260"/>
      <g class="tile-icon" transform="translate(22 168)">
        <circle class="icon-on-dark" cx="22" cy="12" r="11"/>
        <path class="icon-on-dark" d="M0 48 q2 -22 22 -22 q20 0 22 22 z"/>
      </g>
      <text class="tile-label tile-label--on-dark" x="17" y="240">About Darwin</text>
    </g>

    <!-- Tenant information -->
    <g class="nav-tile nav-tile--tenant" transform="translate(424 844)">
      <rect class="tile-dark" width="260" height="260"/>
      <g class="tile-icon" transform="translate(18 180)">
        <circle class="icon-on-dark" cx="42" cy="16" r="15"/>
        <circle fill="var(--charcoal)" cx="42" cy="16" r="6"/>
        <rect class="icon-on-dark" x="0" y="12" width="30" height="8"/>
        <rect class="icon-on-dark" x="2" y="20" width="7" height="9"/>
        <rect class="icon-on-dark" x="13" y="20" width="6" height="7"/>
      </g>
      <text class="tile-label tile-label--on-dark" x="20" y="234">Tenant information</text>
    </g>

    <!-- Properties -->
    <g class="nav-tile nav-tile--properties" transform="translate(179 809)">
      <rect class="tile-light" width="260" height="260"/>
      <g class="tile-icon" transform="translate(42 24)">
        <rect class="icon-on-light" x="0" y="6" width="30" height="44"/>
        <rect class="icon-on-light" x="30" y="18" width="22" height="32"/>
        <g fill="#fff">
          <rect x="5" y="12" width="5" height="5"/><rect x="13" y="12" width="5" height="5"/><rect x="21" y="12" width="5" height="5"/>
          <rect x="5" y="22" width="5" height="5"/><rect x="13" y="22" width="5" height="5"/><rect x="21" y="22" width="5" height="5"/>
          <rect x="5" y="32" width="5" height="5"/><rect x="13" y="32" width="5" height="5"/><rect x="21" y="32" width="5" height="5"/>
          <rect x="35" y="24" width="5" height="5"/><rect x="43" y="24" width="5" height="5"/>
          <rect x="35" y="34" width="5" height="5"/><rect x="43" y="34" width="5" height="5"/>
        </g>
        <rect class="icon-on-light" x="-4" y="50" width="60" height="5"/>
      </g>
      <text class="tile-label tile-label--on-light" transform="translate(20 19) rotate(90)">Properties</text>
    </g>

  </g>
</svg>
</body>
</html>
```